Business Advisory Firm Business Card

A clean, very upscale looking business card. Not crowded.

Please include logo (attached) and:

Daria K. Pellworth
Four Marlow Court
New York, NY 10023
tel: (917) 555-0143
fax: (646) 555-0172
email: dpellworth@quarrystoneconsultants.example
website: www.quarrystoneconsultants.example

Target Market(s)

Business clients. Often real estate development firms, other advisory firms or growing companies that need assistance. I would like a card that looks impressive and confident.

Industry/Entity Type

Business

Colors

Designer to choose colors to be used in the design.

Requirements
Must have
• Impressive and confident. Please include logo.
Should not have
• nothing flashy...

```html
<!DOCTYPE html>
<html lang="en">
<head>
<meta charset="utf-8">
<title>Quarrystone Partners Group — Business Card</title>
<link rel="stylesheet" href="https://fonts.googleapis.com/css2?family=Arimo:wght@400;700&display=swap">
<style>
  :root {
    --backdrop: #e9eef0;
    --card-white: #ffffff;
    --charcoal: #2d373c;
    --wave-grey: #d3d9dc;
    --lime: #c3e41f;
    --lime-dark: #7a9a12;
    --text-light: #ffffff;
  }
  * { margin: 0; padding: 0; box-sizing: border-box; }
  html, body {
    width: 1200px; height: 1000px; overflow: hidden;
    background: var(--backdrop);
  }
  .card {
    position: absolute; left: 57px; top: 182px;
    width: 1086px; height: 635px;
    background: var(--card-white);
    overflow: hidden;
  }
  .card__waves { position: absolute; inset: 0; width: 1086px; height: 635px; }
  .brand {
    position: absolute; left: 0; right: 0; top: 110px;
    display: flex; align-items: center; justify-content: center; gap: 32px;
  }
  .brand__mark {
    width: 110px; height: 110px;
    background: var(--lime-dark);
    flex: none;
  }
  .brand__name {
    font-family: "Arimo", Arial, sans-serif;
    font-weight: 400;
    font-size: 42px;
    line-height: 50px;
    color: var(--charcoal);
    white-space: nowrap;
  }
  .contact {
    position: absolute; left: 0; right: 0; top: 436px;
    text-align: center;
    font-family: "Arimo", Arial, sans-serif;
    color: var(--text-light);
  }
  .contact__name {
    font-weight: 700; font-size: 52px; line-height: 60px;
    color: var(--lime);
  }
  .contact__line { font-size: 25px; line-height: 31px; }
  .contact-strip {
    position: absolute; left: 0; right: 0; bottom: 0; height: 62px;
    background: var(--lime);
    display: flex; align-items: center; justify-content: center;
    font-family: "Arimo", Arial, sans-serif;
    font-size: 22px; color: var(--charcoal);
    white-space: nowrap;
  }
</style>
</head>
<body>
  <div class="card">
    <svg class="card__waves" viewBox="0 0 1086 635" aria-hidden="true">
      <path fill="var(--wave-grey)" d="M0 296 C200 380 380 410 480 405 C650 395 800 330 920 335 C1000 340 1060 380 1086 400 L1086 635 L0 635 Z"/>
      <path fill="var(--charcoal)" d="M0 326 C200 392 350 412 450 410 C620 406 760 356 860 358 C960 360 1040 400 1086 450 L1086 635 L0 635 Z"/>
    </svg>

    <div class="brand">
      <div class="brand__mark"></div>
      <div class="brand__name">Quarrystone Partners Group</div>
    </div>

    <div class="contact">
      <div class="contact__name">Daria K. Pellworth</div>
      <div class="contact__line">Four Marlow Court, New York, NY 10023</div>
      <div class="contact__line">tel: (917) 555-0143 • fax: (646) 555-0172</div>
    </div>

    <div class="contact-strip">
      email: dpellworth@quarrystoneconsultants.example &nbsp;•&nbsp; website: www.quarrystoneconsultants.example
    </div>
  </div>
</body>
</html>
```